!! Innovative new tea company needs packaging design !!

** NB. We need this project as a starting point for our company. We would like to/ intend to have an ongoing relationship with the designer to add to/ change and develop the design in the future on freelance basis pending available workload.

We are in the process of creating a range of functional wellness drinks based on green tea - company name k~. We will have a range of drinks based on green tea attributed to functional effects - boost, detox, immunity etc. Aim of the company is to create a healthy, modern, vibrant company that offers a range of drinks that offer healthy wellness properties, in great tasting fruit flavours.

We need packaging design for the boxes, initially for tea bags. dimensions will be Length – 12cm, Width – 6.75cm, Height – 7.75cm ( please note this means that the box will be TALL / UPRIGHT STANDING)

The brand name is k~ ( to represent green tea + other ingredients / effects). Four initial tea's will be produced that we need to show packaging for :

k~ boost ( rasberry & pomegranite flavour )
k~ immunity ( orange & blueberry )
k~ detox ( apple & blackcurrant )
k~ multi vitamin ( lemon & peach )

We have had the below central brand logo and individual tea logo edits produced already, attached below.

*****Please note we intend the 4 packages to be the same consistent design - only change is on the title of each. For that reason we ONLY REQUEST TO SEE ONE DESIGN ON ONE PRODUCT from a designer to agree on format. Once agreed we will then request you give us the other 3 on agreed format ******

We are aiming to be a very young, vibrant company aiming at the 20 - 40 health conscious consumer. Were taking inspiration from companies like Quillow smoothies and leaf owls and want branding to be in line with those themes.PLEASE LOOK THIS UP TO UNDERSTAND. We need box designs to be completed. Ideally building on the below designs weve had commissioned. However, if a better suggestion on the logo , or a tweak to these will improve the design then we are very much open to it.

Packaging must be, clear white background and bold colors along the line of each flavour teas colour ( ie red for boost, yellow multi vitamin etc). We would ideally like the top and one side ( ONLY ) of the box to be coloured background ( matching the drink colour ). We are wanting simple and clear design FAIRLY MINIMALIST to convey the point of the brand to be simple clear and healthy ingredients. At the same time it must clearly stand out on a shelf. Lighthearted and not too serious, ideally simple, fun illustrated drawings ( ideally outlines/very simple drawings) of the fruit aligned to each flavour and any other branding / mascot logo design that you can suggest.

Also possible cartoon/simple illustration tea leaf somewhere on the box.

We need packaging for the 4 teas - 1 consistent design and theme, with only changes to color and a few illustrations per box.

Please note - We want text font to be funky, friendly, soft - various sizes on the text on the boxes - NOT everything the same size and generic font.

text to go on the box

( front of box):

- main t+boost/immunity etc logo
.(tagline underneath) Wellness drinks

- * Green tea with vitamins drink

- * Natural Ceylon green tea with added vitamins and herbs to give you the best start to your day.

- * 5 reasons to drink this!!
100% natural ingredients
x% of your RDA of x
x mg of antioxidants to keep your heart healthy.
Naturally sweet taste
only x calories per cup!

(side of box)

Ingredients

We use only the finest hand picked ceylon green tea and mix it with natural fruit pieces, a hint of natural flavouring as our base. We add the goodness of burdock root and echinacea to help build your body's defenses and sweeten it with a dash of the south american stevia leaf to give a great tasting drink that will do you some good!

( side of box )

Nutrition Facts

Serving Size: 1 tea bag (4g)

Makes: 8 fl. oz.

Servings Per Container: 25

Amount Per Serving
Calories 0

% Daily Value*
Total Fat 0g
0%
Sodium 0mg
5%
Total Carb. 0g
0%
Sugars 10g
Protein 0g

* Percent Daily Values are based on a 2,000 calorie diet.

The above is how we forsee the packaging for now. However - anything that you can reccommend that is innovative to help us stand out to a young , trendy audience will be welcome.

Please message with any questions or comments.
Updates

Dear All - Please note - we have updated the brief with the packaging die line for your reference. Please note the box will be upstanding so designs should accomodate for a tall box.

Dear All - To reiterate key points of the brief - We request the deign to be stand out here. Majority white background with splashes/swirls/blotches of colour ( whatever design suggested ).Further to that, illustrations ( drawings - not pictures ) of fruit / tea leaves to stay in line with young, funky image. 

Overall theme is young, bright and modern - we need the packaging to reflect this. Not just standard text font and background colouring.
Any more clarity needed please contact us. 

Reason: Dear All We have increased the budget for this project and extended the deadline by additional 7 days. To date we have not received the designs we are happy with so want to give all added time to revise - follow the brief - and resubmit. Due to quality of designs received so far - we will not guarantee payment yet - HOWEVER - Intention is to get this completed for the business by next week latest- for that reason, as soon as someone has submitted a design that is at least along the right lines - we will then move to guarantee payment. Please also note - we intend to / hope to work with the designer directly on ongoing projects for the company so want a good - long term relationship from this. Good luck and please contact us if any more information needed. Regards

Dear all

Please can we request that for the sides of the box with a white background - text is in a green colour ( same shade as the original k~ logo green ). We would like this to be our standard font colour against white background. 

Obviously, please add colour where you see fit but we want a clean , consistent font across the boxes and eventually our web site. 

For the coloured backgrounds of the side and top - will leave up to you whatever colour font looks best. 

Reason: Deadline extended to provide some more feedback to designers. No decision yet made.

Target Market(s)

Young, health conscious individuals.

Industry/Entity Type

It Company

```html
<!DOCTYPE html>
<html lang="en">
<head>
<meta charset="utf-8">
<title>k~ Wellness Drinks – Box Panels</title>
<link href="https://fonts.googleapis.com/css2?family=Baloo+2:wght@600;700;800&family=Kalam:wght@700&display=swap" rel="stylesheet">
<style>
  :root {
    --bg: #ededed;
    --white: #ffffff;
    --leaf-green: #8cc63f;
    --boost: #e3175f;
    --immunity: #f26818;
    --multi: #e2da24;
    --detox: #2a9fc0;
  }
  * { box-sizing: border-box; margin: 0; padding: 0; }
  html, body { width: 1200px; height: 1000px; overflow: hidden; }
  body {
    background: linear-gradient(180deg, #ffffff 0%, var(--bg) 100%);
    font-family: "Kalam", cursive;
  }
  .range {
    position: absolute;
    left: 12px; top: 315px;
    display: flex; gap: 25px;
  }
  .box-net {
    --flavour: var(--boost);
    display: grid;
    grid-template-columns: 90px 185px;
    grid-template-rows: 80px 290px;
  }
  .box-net.immunity { --flavour: var(--immunity); }
  .box-net.multi-vitamin { --flavour: var(--multi); }
  .box-net.detox { --flavour: var(--detox); }

  /* top panel */
  .box-top {
    grid-column: 2; grid-row: 1;
    background: var(--flavour); color: var(--white);
    display: flex; flex-direction: column; align-items: center; justify-content: center;
    box-shadow: 0 2px 6px rgba(0,0,0,0.12);
  }
  .box-top .top-brand {
    display: flex; align-items: center; gap: 4px;
    font-family: "Baloo 2", sans-serif; font-weight: 800; font-size: 22px; line-height: 1;
  }
  .box-top .top-brand .dot { width: 8px; height: 8px; border-radius: 50%; background: var(--white); }
  .box-top .top-title {
    font-family: "Baloo 2", sans-serif; font-weight: 800; font-size: 22px; line-height: 1;
    margin-top: 2px;
  }
  .box-top .top-line { font-size: 10px; line-height: 1.2; margin-top: 2px; }

  /* side panel */
  .box-side {
    grid-column: 1; grid-row: 2;
    background: var(--white);
    padding: 7px 6px;
    color: var(--leaf-green);
    font-family: "Baloo 2", sans-serif; font-weight: 700;
    box-shadow: 0 2px 6px rgba(0,0,0,0.12);
    border-right: 1px solid #e6e6e6;
  }
  .side-heading {
    font-family: "Baloo 2", sans-serif; font-weight: 800;
    font-size: 11px; line-height: 13px; color: var(--flavour);
  }
  .ingredients { font-size: 6px; line-height: 7.4px; margin: 2px 0 6px; }
  .nutrition { font-size: 6px; line-height: 7.6px; }
  .nutrition .row { display: flex; justify-content: space-between; border-bottom: 0.5px solid var(--leaf-green); }
  .nutrition .note { margin-top: 2px; line-height: 7px; }

  /* front panel */
  .box-front {
    grid-column: 2; grid-row: 2;
    position: relative;
    background: var(--white);
    box-shadow: 0 2px 6px rgba(0,0,0,0.12);
    overflow: hidden;
  }
  .reasons-corner {
    position: absolute; right: 0; top: 0;
    width: 85px; height: 95px;
  }
  .reasons-corner svg { position: absolute; inset: 0; }
  .reasons-text {
    position: absolute; right: 3px; top: 6px; width: 70px;
    color: var(--white); text-align: center;
    font-size: 11px; line-height: 12px;
    transform: rotate(-12deg);
  }
  .reasons-text .count { display: block; font-size: 15px; line-height: 15px; }

  .brand-mark {
    position: absolute; left: 14px; top: 22px;
    display: flex; align-items: center; gap: 4px;
  }
  .brand-mark .dot { width: 11px; height: 11px; border-radius: 50%; background: var(--flavour); }
  .brand-mark .name {
    font-family: "Baloo 2", sans-serif; font-weight: 800;
    font-size: 34px; line-height: 1; color: var(--flavour);
  }
  .tagline {
    position: absolute; left: 14px; top: 82px;
    color: var(--leaf-green); font-size: 14px; line-height: 16px;
  }
  .product-title {
    position: absolute; left: 13px; top: 96px;
    font-family: "Baloo 2", sans-serif; font-weight: 800;
    font-size: 30px; line-height: 1.1; color: var(--flavour);
    white-space: nowrap;
  }
  .multi-vitamin .product-title { font-size: 24px; top: 100px; }
  .fruit-illustration {
    position: absolute; left: 28px; top: 141px;
    width: 130px; height: 56px; border-radius: 28px;
    background: linear-gradient(90deg, #e6f3d3 0%, color-mix(in srgb, var(--flavour) 22%, white) 100%);
  }
  .drink-line {
    position: absolute; left: 0; right: 0; top: 202px;
    text-align: center; color: var(--leaf-green); font-size: 11.5px; line-height: 14px;
  }
  .drink-line svg { display: block; margin: -2px auto 0; }
  .description {
    position: absolute; left: 12px; right: 12px; top: 224px;
    text-align: center; color: var(--leaf-green);
    font-family: "Baloo 2", sans-serif; font-weight: 700;
    font-size: 7.5px; line-height: 9.5px;
  }
  .flavour-band {
    position: absolute; left: 0; right: 0; bottom: 0; height: 30px;
    background: var(--flavour); color: var(--white);
    display: flex; align-items: center; justify-content: center;
    font-size: 13.5px;
  }
</style>
</head>
<body>
<main class="range">

  <section class="box-net boost">
    <header class="box-top">
      <div class="top-brand"><span>k~</span><span class="dot"></span></div>
      <p class="top-title">boost</p>
      <p class="top-line">Green tea with vitamins drink</p>
    </header>
    <aside class="box-side">
      <h3 class="side-heading">Ingredients</h3>
      <p class="ingredients">We use only the finest hand picked ceylon green tea and mix it with natural fruit pieces, a hint of natural flavouring as our base. We add the goodness of burdock root and echinacea to help build your body's defenses and sweeten it with a dash of the south american stevia leaf to give a great tasting drink that will do you some good!</p>
      <h3 class="side-heading">Nutrition Facts</h3>
      <div class="nutrition">
        <p>Serving Size: 1 tea bag (4g)</p><p>Makes: 8 fl. oz.</p><p>Servings Per Container: 25</p>
        <div class="row"><span>Calories</span><span>0</span></div>
        <div class="row"><span>Total Fat 0g</span><span>0%</span></div>
        <div class="row"><span>Sodium 0mg</span><span>5%</span></div>
        <div class="row"><span>Total Carb. 0g</span><span>0%</span></div>
        <div class="row"><span>Sugars 10g</span><span></span></div>
        <div class="row"><span>Protein 0g</span><span></span></div>
        <p class="note">* Percent Daily Values are based on a 2,000 calorie diet.</p>
      </div>
    </aside>
    <article class="box-front">
      <div class="reasons-corner">
        <svg width="85" height="95" viewBox="0 0 130 150" preserveAspectRatio="none"><path d="M10 0 H130 V150 C70 140 25 80 10 0 Z" fill="var(--flavour)"/></svg>
        <p class="reasons-text"><span class="count">5</span>Reasons<br>to drink<br>this!! →</p>
      </div>
      <div class="brand-mark"><span class="name">k~</span><span class="dot"></span></div>
      <p class="tagline">Wellness Drinks</p>
      <h2 class="product-title">boost</h2>
      <div class="fruit-illustration" role="img" aria-label="Outline drawing of tea leaves, raspberries and a pomegranate"></div>
      <p class="drink-line">Green tea with vitamins drink
        <svg width="50" height="5" viewBox="0 0 60 6"><path d="M2 4 Q30 0 58 3" stroke="var(--flavour)" stroke-width="2" fill="none" stroke-linecap="round"/></svg></p>
      <p class="description">Natural Ceylon green tea with added vitamins and herbs to give you the best start to your day.</p>
      <div class="flavour-band">Raspberry &amp; Pomegranite</div>
    </article>
  </section>

  <section class="box-net immunity">
    <header class="box-top">
      <div class="top-brand"><span>k~</span><span class="dot"></span></div>
      <p class="top-title">immunity</p>
      <p class="top-line">Green tea with vitamins drink</p>
    </header>
    <aside class="box-side">
      <h3 class="side-heading">Ingredients</h3>
      <p class="ingredients">We use only the finest hand picked ceylon green tea and mix it with natural fruit pieces, a hint of natural flavouring as our base. We add the goodness of burdock root and echinacea to help build your body's defenses and sweeten it with a dash of the south american stevia leaf to give a great tasting drink that will do you some good!</p>
      <h3 class="side-heading">Nutrition Facts</h3>
      <div class="nutrition">
        <p>Serving Size: 1 tea bag (4g)</p><p>Makes: 8 fl. oz.</p><p>Servings Per Container: 25</p>
        <div class="row"><span>Calories</span><span>0</span></div>
        <div class="row"><span>Total Fat 0g</span><span>0%</span></div>
        <div class="row"><span>Sodium 0mg</span><span>5%</span></div>
        <div class="row"><span>Total Carb. 0g</span><span>0%</span></div>
        <div class="row"><span>Sugars 10g</span><span></span></div>
        <div class="row"><span>Protein 0g</span><span></span></div>
        <p class="note">* Percent Daily Values are based on a 2,000 calorie diet.</p>
      </div>
    </aside>
    <article class="box-front">
      <div class="reasons-corner">
        <svg width="85" height="95" viewBox="0 0 130 150" preserveAspectRatio="none"><path d="M10 0 H130 V150 C70 140 25 80 10 0 Z" fill="var(--flavour)"/></svg>
        <p class="reasons-text"><span class="count">5</span>Reasons<br>to drink<br>this!! →</p>
      </div>
      <div class="brand-mark"><span class="name">k~</span><span class="dot"></span></div>
      <p class="tagline">Wellness Drinks</p>
      <h2 class="product-title">immunity</h2>
      <div class="fruit-illustration" role="img" aria-label="Outline drawing of tea leaves, blueberries and an orange"></div>
      <p class="drink-line">Green tea with vitamins drink
        <svg width="50" height="5" viewBox="0 0 60 6"><path d="M2 4 Q30 0 58 3" stroke="var(--flavour)" stroke-width="2" fill="none" stroke-linecap="round"/></svg></p>
      <p class="description">Natural Ceylon green tea with added vitamins and herbs to give you the best start to your day.</p>
      <div class="flavour-band">Orange &amp; Blueberry</div>
    </article>
  </section>

  <section class="box-net multi-vitamin">
    <header class="box-top">
      <div class="top-brand"><span>k~</span><span class="dot"></span></div>
      <p class="top-title">multi vitamin</p>
      <p class="top-line">Green tea with vitamins drink</p>
    </header>
    <aside class="box-side">
      <h3 class="side-heading">Ingredients</h3>
      <p class="ingredients">We use only the finest hand picked ceylon green tea and mix it with natural fruit pieces, a hint of natural flavouring as our base. We add the goodness of burdock root and echinacea to help build your body's defenses and sweeten it with a dash of the south american stevia leaf to give a great tasting drink that will do you some good!</p>
      <h3 class="side-heading">Nutrition Facts</h3>
      <div class="nutrition">
        <p>Serving Size: 1 tea bag (4g)</p><p>Makes: 8 fl. oz.</p><p>Servings Per Container: 25</p>
        <div class="row"><span>Calories</span><span>0</span></div>
        <div class="row"><span>Total Fat 0g</span><span>0%</span></div>
        <div class="row"><span>Sodium 0mg</span><span>5%</span></div>
        <div class="row"><span>Total Carb. 0g</span><span>0%</span></div>
        <div class="row"><span>Sugars 10g</span><span></span></div>
        <div class="row"><span>Protein 0g</span><span></span></div>
        <p class="note">* Percent Daily Values are based on a 2,000 calorie diet.</p>
      </div>
    </aside>
    <article class="box-front">
      <div class="reasons-corner">
        <svg width="85" height="95" viewBox="0 0 130 150" preserveAspectRatio="none"><path d="M10 0 H130 V150 C70 140 25 80 10 0 Z" fill="var(--flavour)"/></svg>
        <p class="reasons-text"><span class="count">5</span>Reasons<br>to drink<br>this!! →</p>
      </div>
      <div class="brand-mark"><span class="name">k~</span><span class="dot"></span></div>
      <p class="tagline">Wellness Drinks</p>
      <h2 class="product-title">multi vitamin</h2>
      <div class="fruit-illustration" role="img" aria-label="Outline drawing of tea leaves, a peach half and a lemon"></div>
      <p class="drink-line">Green tea with vitamins drink
        <svg width="50" height="5" viewBox="0 0 60 6"><path d="M2 4 Q30 0 58 3" stroke="var(--flavour)" stroke-width="2" fill="none" stroke-linecap="round"/></svg></p>
      <p class="description">Natural Ceylon green tea with added vitamins and herbs to give you the best start to your day.</p>
      <div class="flavour-band">Lemon &amp; Peach</div>
    </article>
  </section>

  <section class="box-net detox">
    <header class="box-top">
      <div class="top-brand"><span>k~</span><span class="dot"></span></div>
      <p class="top-title">detox</p>
      <p class="top-line">Green tea with vitamins drink</p>
    </header>
    <aside class="box-side">
      <h3 class="side-heading">Ingredients</h3>
      <p class="ingredients">We use only the finest hand picked ceylon green tea and mix it with natural fruit pieces, a hint of natural flavouring as our base. We add the goodness of burdock root and echinacea to help build your body's defenses and sweeten it with a dash of the south american stevia leaf to give a great tasting drink that will do you some good!</p>
      <h3 class="side-heading">Nutrition Facts</h3>
      <div class="nutrition">
        <p>Serving Size: 1 tea bag (4g)</p><p>Makes: 8 fl. oz.</p><p>Servings Per Container: 25</p>
        <div class="row"><span>Calories</span><span>0</span></div>
        <div class="row"><span>Total Fat 0g</span><span>0%</span></div>
        <div class="row"><span>Sodium 0mg</span><span>5%</span></div>
        <div class="row"><span>Total Carb. 0g</span><span>0%</span></div>
        <div class="row"><span>Sugars 10g</span><span></span></div>
        <div class="row"><span>Protein 0g</span><span></span></div>
        <p class="note">* Percent Daily Values are based on a 2,000 calorie diet.</p>
      </div>
    </aside>
    <article class="box-front">
      <div class="reasons-corner">
        <svg width="85" height="95" viewBox="0 0 130 150" preserveAspectRatio="none"><path d="M10 0 H130 V150 C70 140 25 80 10 0 Z" fill="var(--flavour)"/></svg>
        <p class="reasons-text"><span class="count">5</span>Reasons<br>to drink<br>this!! →</p>
      </div>
      <div class="brand-mark"><span class="name">k~</span><span class="dot"></span></div>
      <p class="tagline">Wellness Drinks</p>
      <h2 class="product-title">detox</h2>
      <div class="fruit-illustration" role="img" aria-label="Outline drawing of tea leaves, blackcurrants and an apple"></div>
      <p class="drink-line">Green tea with vitamins drink
        <svg width="50" height="5" viewBox="0 0 60 6"><path d="M2 4 Q30 0 58 3" stroke="var(--flavour)" stroke-width="2" fill="none" stroke-linecap="round"/></svg></p>
      <p class="description">Natural Ceylon green tea with added vitamins and herbs to give you the best start to your day.</p>
      <div class="flavour-band">Apple &amp; Blackcurrant</div>
    </article>
  </section>

</main>
</body>
</html>
```